velmorino.eu :: Design ideas (no coding) for key pages of Personalized greeting cards online store

We need your vision on modern, clean, easy to read user interface (UI) for online service of personalized printed products, like greeting cards, postcards, fridge magnets, clips and etc.
Your vision should include UI presentation for:
- Home page with login (including soc nets)
- Product Designer page
- Cart pages (products and address selection)
- Example of general internal page (pricing, terms, etc)
- Artist info and portfolio page
We are looking for ideas we will love, NOT complete design of a whole site.
Top design/vision will we used as a basement for separate contract on complete design of the site.

UI should be based on existing functionality with some extent. It should not break ideas or methods used on prototype but designers are free to offer own product presentations, designer’s layout and cart views.

Prototype:
English: http://velmorino.eu
Russian: http://velmorino.ru
Lithuanian: http://velmorino.lt

Target Market(s)

People of 16-45 y.o. who likes to be distinctive, personal.

Industry/Entity Type

Store

Requirements
Must have
• Your work should meet attached requirements.
Site is multilingual. Wording should assume varieties in length on different languages.
Clean and easy to read UI
Flat design preferrably
Should be based on assets which are free or available for royalty-free licensing
Should not have
• heavy, meaningless 3D and shadow effects
Show NOT copy sites like: plonkra.com, tarnwick.co.uk

```html
<!DOCTYPE html>
<html lang="en">
<head>
<meta charset="utf-8">
<title>velmorino — Authors</title>
<link href="https://fonts.googleapis.com/css2?family=Carlito:wght@400;700&family=Open+Sans:wght@300;400;600;700&display=swap" rel="stylesheet">
<style>
  :root {
    --page-bg: #f3f3f2;
    --panel: #ffffff;
    --brand-red: #a31e14;
    --text: #222222;
    --muted: #7a7a7a;
    --price: #1c8c8f;
    --line: #d8d8d8;
    --card-border: #e3e3e3;
  }
  * { box-sizing: border-box; margin: 0; padding: 0; }
  html, body { width: 1054px; height: 1200px; overflow: hidden; }
  body {
    background: var(--page-bg);
    font-family: "Carlito", "Calibri", sans-serif;
    color: var(--text);
    position: relative;
  }
  .site { position: absolute; left: 97px; top: 0; width: 860px; }

  .brand {
    position: absolute; left: 0; top: 72px;
    display: flex; align-items: center; gap: 6px;
    font-family: "Carlito", sans-serif; font-size: 21px; color: var(--brand-red);
  }
  .brand-mark { width: 10px; height: 10px; background: var(--brand-red); }
  .tagline {
    position: absolute; left: 225px; top: 40px;
    font-family: "Carlito", sans-serif; font-size: 16px; color: var(--brand-red);
  }

  .main-nav { position: absolute; left: 0; top: 83px; width: 860px; height: 31px; }
  .nav-link {
    position: absolute; top: 0; height: 31px; line-height: 33px;
    font-family: "Open Sans", sans-serif; font-weight: 600; font-size: 11.5px;
    color: var(--text); text-decoration: none; letter-spacing: .2px;
  }
  .nav-products { left: 143px; }
  .nav-authors {
    left: 219px; width: 86px; text-align: center;
    background: var(--brand-red); color: #fff; border-radius: 3px 3px 0 0;
  }
  .account {
    position: absolute; right: 0; top: 9px;
    display: flex; align-items: center; gap: 18px;
    font-family: "Open Sans", sans-serif; font-size: 11.5px; color: var(--muted);
  }
  .account span { display: inline-flex; align-items: center; gap: 5px; }
  .cart b { color: var(--brand-red); font-weight: 600; }
  .nav-rule { position: absolute; left: 0; top: 113px; width: 860px; height: 2px; background: var(--brand-red); }

  .page-title {
    position: absolute; left: 0; top: 115px; width: 860px; height: 80px;
    background: var(--panel); text-align: center; line-height: 84px;
    font-family: "Open Sans", sans-serif; font-weight: 300; font-size: 18.5px; color: #333;
  }
  .hero {
    position: absolute; left: 0; top: 195px; width: 860px; height: 210px;
    background: linear-gradient(90deg, #efe6cf 0%, #ece2c8 40%, #cfe3ea 56%, #bcdcec 100%);
  }

  .author { position: absolute; left: 0; width: 860px; }
  .author-1 { top: 418px; }
  .author-2 { top: 808px; }
  .author-name { font-size: 15.5px; font-weight: 700; line-height: 22px; }
  .author-bio { margin-top: 4px; font-size: 12.3px; line-height: 18.5px; text-align: justify; }

  .card-grid { position: absolute; left: 0; top: 113px; display: flex; gap: 19px; }
  .card { width: 201px; height: 248px; background: var(--panel); border: 1px solid var(--card-border); }
  .card-art { width: 199px; height: 199px; }
  .art-cow { background: linear-gradient(180deg, #8fb4d8 0%, #b8cde0 35%, #8dc052 55%, #2f8a22 100%); }
  .art-tree { background: radial-gradient(circle at 50% 40%, #9fb3a6 0%, #b7b8b0 35%, #f0b8b6 70%, #f2c3c0 100%); }
  .art-towers { background: linear-gradient(180deg, #b9dcec 0%, #e4eef0 45%, #d8ded2 75%, #eef0ea 100%); }
  .art-cat { background: linear-gradient(180deg, #efe8d4 0%, #e8dfc7 72%, #c8b890 82%, #b99a66 100%); }
  .card-meta {
    display: flex; justify-content: space-between; align-items: center;
    height: 47px; padding: 0 13px 0 15px;
  }
  .price { font-family: "Open Sans", sans-serif; font-weight: 700; font-size: 13px; color: var(--price); }
  .card-actions { display: flex; gap: 8px; align-items: center; }

  .divider { position: absolute; left: 0; top: 797px; width: 860px; height: 1px; background: var(--line); }
</style>
</head>
<body>
<div class="site">
  <div class="brand"><span class="brand-mark"></span>velmorino</div>
  <p class="tagline">The individual greeting cards according to your mood</p>

  <nav class="main-nav">
    <a class="nav-link nav-products" href="#">PRODUCTS</a>
    <a class="nav-link nav-authors" href="#">AUTHORS</a>
    <div class="account">
      <span class="sign-in">
        <svg width="10" height="11" viewBox="0 0 10 11"><circle cx="5" cy="3" r="2.5" fill="#a31e14"/><path d="M1 11c0-3 2-4.5 4-4.5S9 8 9 11z" fill="#a31e14"/></svg>
        SIGN IN
      </span>
      <span class="cart">
        <svg width="18" height="13" viewBox="0 0 18 13"><path d="M0 1h3l2 8h10l2-6H5" fill="none" stroke="#a31e14" stroke-width="2"/><path d="M4.5 3h12l-1.8 5H6z" fill="#a31e14"/><circle cx="7" cy="11.5" r="1.5" fill="#a31e14"/><circle cx="14" cy="11.5" r="1.5" fill="#a31e14"/></svg>
        <b>CART:</b> 0 ITEMS - $0.00
      </span>
    </div>
  </nav>
  <div class="nav-rule"></div>

  <h1 class="page-title">WE ARE HAPPY WITH OUR AUTHORS</h1>
  <div class="hero" role="img" aria-label="Wide illustration: a white cat beside a food bowl and colourful whimsical towers under a blue sky"></div>

  <section class="author author-1">
    <h2 class="author-name">Mira Tavelsky</h2>
    <p class="author-bio">My name is Mira Tavelsky and I’m an illustrator located in Israel. I was born in Vilnius, Lithuania, where I grew up.<br>I've been drawing ever since I can remember. It was definitely an experience that helped to shape my love of illustration and type. I’m an architect, but after all I decided to follow my dreams and nowadays an illustration is my hobby. I create cute, whimsical and just plain fun art kids and I've been putting smiles on faces. I can only say: do what you do best and love and the rest will follow.</p>
    <div class="card-grid">
      <article class="card"><div class="card-art art-cow" role="img" aria-label="Card illustration: a cow on green hills"></div><div class="card-meta"><span class="price">€ 2.99</span><span class="card-actions"><svg width="15" height="12" viewBox="0 0 15 12"><path d="M1 4h3l4-3v10L4 8H1z" fill="#999"/><path d="M10 3.5c1.5 1.5 1.5 3.5 0 5M12 2c2.3 2.3 2.3 5.7 0 8" fill="none" stroke="#999" stroke-width="1.2"/></svg><svg width="14" height="13" viewBox="0 0 14 13"><path d="M1 12V5.5L7 1l6 4.5V12z" fill="none" stroke="#999" stroke-width="1.5"/></svg></span></div></article>
      <article class="card"><div class="card-art art-tree" role="img" aria-label="Card illustration: a spiral tree with red hearts on pink"></div><div class="card-meta"><span class="price">€ 0.99</span><span class="card-actions"><svg width="15" height="12" viewBox="0 0 15 12"><path d="M1 4h3l4-3v10L4 8H1z" fill="#999"/><path d="M10 3.5c1.5 1.5 1.5 3.5 0 5M12 2c2.3 2.3 2.3 5.7 0 8" fill="none" stroke="#999" stroke-width="1.2"/></svg><svg width="14" height="13" viewBox="0 0 14 13"><path d="M1 12V5.5L7 1l6 4.5V12z" fill="none" stroke="#999" stroke-width="1.5"/></svg></span></div></article>
      <article class="card"><div class="card-art art-towers" role="img" aria-label="Card illustration: whimsical towers with Bon Voyage lettering"></div><div class="card-meta"><span class="price">€ 0.99</span><span class="card-actions"><svg width="15" height="12" viewBox="0 0 15 12"><path d="M1 4h3l4-3v10L4 8H1z" fill="#999"/><path d="M10 3.5c1.5 1.5 1.5 3.5 0 5M12 2c2.3 2.3 2.3 5.7 0 8" fill="none" stroke="#999" stroke-width="1.2"/></svg><svg width="14" height="13" viewBox="0 0 14 13"><path d="M1 12V5.5L7 1l6 4.5V12z" fill="none" stroke="#999" stroke-width="1.5"/></svg></span></div></article>
      <article class="card"><div class="card-art art-cat" role="img" aria-label="Card illustration: a cat by its bowl with Don't forget me lettering"></div><div class="card-meta"><span class="price">€ 0.99</span><span class="card-actions"><svg width="15" height="12" viewBox="0 0 15 12"><path d="M1 4h3l4-3v10L4 8H1z" fill="#999"/><path d="M10 3.5c1.5 1.5 1.5 3.5 0 5M12 2c2.3 2.3 2.3 5.7 0 8" fill="none" stroke="#999" stroke-width="1.2"/></svg><svg width="14" height="13" viewBox="0 0 14 13"><path d="M1 12V5.5L7 1l6 4.5V12z" fill="none" stroke="#999" stroke-width="1.5"/></svg></span></div></article>
    </div>
  </section>

  <div class="divider"></div>

  <section class="author author-2">
    <h2 class="author-name">Mira Tavelsky</h2>
    <p class="author-bio">My name is Mira Tavelsky and I’m an illustrator located in Israel. I was born in Vilnius, Lithuania, where I grew up.<br>I've been drawing ever since I can remember. It was definitely an experience that helped to shape my love of illustration and type. I’m an architect, but after all I decided to follow my dreams and nowadays an illustration is my hobby. I create cute, whimsical and just plain fun art kids and I've been putting smiles on faces. I can only say: do what you do best and love and the rest will follow.</p>
    <div class="card-grid">
      <article class="card"><div class="card-art art-cow" role="img" aria-label="Card illustration: a cow on green hills"></div><div class="card-meta"><span class="price">€ 2.99</span><span class="card-actions"><svg width="15" height="12" viewBox="0 0 15 12"><path d="M1 4h3l4-3v10L4 8H1z" fill="#999"/><path d="M10 3.5c1.5 1.5 1.5 3.5 0 5M12 2c2.3 2.3 2.3 5.7 0 8" fill="none" stroke="#999" stroke-width="1.2"/></svg><svg width="14" height="13" viewBox="0 0 14 13"><path d="M1 12V5.5L7 1l6 4.5V12z" fill="none" stroke="#999" stroke-width="1.5"/></svg></span></div></article>
      <article class="card"><div class="card-art art-tree" role="img" aria-label="Card illustration: a spiral tree with red hearts on pink"></div><div class="card-meta"><span class="price">€ 0.99</span><span class="card-actions"><svg width="15" height="12" viewBox="0 0 15 12"><path d="M1 4h3l4-3v10L4 8H1z" fill="#999"/><path d="M10 3.5c1.5 1.5 1.5 3.5 0 5M12 2c2.3 2.3 2.3 5.7 0 8" fill="none" stroke="#999" stroke-width="1.2"/></svg><svg width="14" height="13" viewBox="0 0 14 13"><path d="M1 12V5.5L7 1l6 4.5V12z" fill="none" stroke="#999" stroke-width="1.5"/></svg></span></div></article>
      <article class="card"><div class="card-art art-towers" role="img" aria-label="Card illustration: whimsical towers with Bon Voyage lettering"></div><div class="card-meta"><span class="price">€ 0.99</span><span class="card-actions"><svg width="15" height="12" viewBox="0 0 15 12"><path d="M1 4h3l4-3v10L4 8H1z" fill="#999"/><path d="M10 3.5c1.5 1.5 1.5 3.5 0 5M12 2c2.3 2.3 2.3 5.7 0 8" fill="none" stroke="#999" stroke-width="1.2"/></svg><svg width="14" height="13" viewBox="0 0 14 13"><path d="M1 12V5.5L7 1l6 4.5V12z" fill="none" stroke="#999" stroke-width="1.5"/></svg></span></div></article>
      <article class="card"><div class="card-art art-cat" role="img" aria-label="Card illustration: a cat by its bowl with Don't forget me lettering"></div><div class="card-meta"><span class="price">€ 0.99</span><span class="card-actions"><svg width="15" height="12" viewBox="0 0 15 12"><path d="M1 4h3l4-3v10L4 8H1z" fill="#999"/><path d="M10 3.5c1.5 1.5 1.5 3.5 0 5M12 2c2.3 2.3 2.3 5.7 0 8" fill="none" stroke="#999" stroke-width="1.2"/></svg><svg width="14" height="13" viewBox="0 0 14 13"><path d="M1 12V5.5L7 1l6 4.5V12z" fill="none" stroke="#999" stroke-width="1.5"/></svg></span></div></article>
    </div>
  </section>
</div>
</body>
</html>
```